Website for Foodstuff Import-Export Company *

We need a website for our company which imports and sell ( edible oil , ketchup , mayonnaise and pulses ). our current website is velmorix.pl , we need a website which has corporate appearance with good quality products.

Target Market(s)

European Wholesalers , Supermarket Chains,

Coding

Coded - Design and coding required

Number of Pages Required

1 page

```html
<!DOCTYPE html>
<html lang="en">
<head>
<meta charset="utf-8">
<title>Velmorix – Foodstuff Import &amp; Export</title>
<link href="https://fonts.googleapis.com/css2?family=Lato:wght@400;700;900&display=swap" rel="stylesheet">
<style>
:root{
  --ink:#2b2b2b;
  --text:#333333;
  --pink:#ea3e80;
  --orange:#f8a83a;
  --yellow:#f8c73a;
  --green:#3aa945;
  --blue:#5fc0e0;
  --header-bg:#f4f4f4;
  --frame:#3a3a3a;
}
*{margin:0;padding:0;box-sizing:border-box}
html,body{width:1200px;height:3792px;overflow:hidden}
body{position:relative;background:#fff;font-family:'Lato',sans-serif;color:var(--text)}
.abs{position:absolute}
.top-line{left:0;top:0;width:1200px;height:4px;background:linear-gradient(90deg,var(--pink),var(--orange),var(--yellow),var(--blue),var(--green))}
.site-header{left:0;top:4px;width:1200px;height:136px;background:var(--header-bg)}
.brand{left:113px;top:50px;display:flex;align-items:center;gap:10px;font-weight:900;font-size:30px;color:var(--green);letter-spacing:1px}
.brand-dot{width:26px;height:26px;border-radius:50%;background:var(--green)}
.nav{top:50px;height:50px;display:flex;align-items:center;font-size:15px;color:var(--ink);text-transform:uppercase}
.pill{background:linear-gradient(90deg,var(--pink),var(--orange));color:#fff;border-radius:26px;display:flex;align-items:center;justify-content:center;font-weight:700}
.nav-home{left:643px;width:96px;justify-content:center}
.hero{left:0;top:140px;width:1200px;height:596px;background:radial-gradient(ellipse at 62% 20%,#e8d78a 0%,#b9b35a 25%,#6f8a3c 50%,#3f5a2a 75%),linear-gradient(#6b8a3a,#3a4a2a)}
.hero-base{left:0;top:590px;width:1200px;height:146px;background:linear-gradient(90deg,#2f4a22,#d84a3a 35%,#e9e3dc 55%,#c84034 80%,#3b5226)}
.hero-caption{left:210px;top:402px;width:776px;height:182px;background:rgba(40,40,40,.82);color:#fff;font-weight:700;font-size:53px;line-height:62px;text-align:center;display:flex;align-items:center;justify-content:center}
.section-title{left:0;width:1200px;text-align:center;font-weight:700;font-size:52px;color:var(--ink)}
.intro{left:150px;top:890px;width:900px;text-align:center;font-size:20px;line-height:27.5px;color:var(--ink)}
.btn{width:192px;height:52px;font-size:20px;text-transform:uppercase}
.cat{border:3px solid var(--yellow);background:#fff}
.cat-fill{position:absolute;left:8px;top:8px;right:8px;bottom:8px;border-radius:6px}
.cat-label{position:absolute;left:0;right:0;bottom:0;height:70px;background:var(--yellow);color:var(--ink);font-weight:700;font-size:36px;display:flex;align-items:center;justify-content:center}
.warehouse{left:0;top:1705px;width:1200px;height:577px;background:linear-gradient(180deg,#6d7a6a 0%,#8a4a4a 45%,#7b6a6a 75%,#8a8a8e 100%)}
.warehouse::after{content:"";position:absolute;inset:0;background:linear-gradient(90deg,rgba(190,60,80,.35),rgba(90,140,90,.35))}
.band-title{left:0;top:1935px;width:1200px;text-align:center;color:#fff;font-weight:700;font-size:50px}
.product{border:1.5px solid var(--frame);background:#fff}
.product-fill{position:absolute;left:30px;top:30px;right:30px;bottom:30px;border-radius:10px}
.product-name{top:2762px;width:226px;text-align:center;font-weight:700;font-size:20px;color:var(--ink)}
.map{left:0;top:2925px;width:1200px;height:453px;background:linear-gradient(135deg,#eef0ea,#e6e9e2 40%,#f1ece0)}
.contact-title{left:125px;top:3424px;font-weight:700;font-size:40px;color:var(--ink)}
.col-head{top:3502px;font-size:20px;color:var(--ink);font-weight:700}
.line{font-size:14px;color:var(--ink);display:flex;align-items:flex-start;gap:14px;line-height:21px}
.line svg{flex:none;margin-top:3px}
.site-footer{left:0;top:3720px;width:1200px;height:72px;background:linear-gradient(90deg,var(--pink),var(--orange) 25%,#f4c95a 40%,var(--blue) 65%,var(--green));color:#fff;font-size:15px;display:flex;align-items:center;justify-content:center}
</style>
</head>
<body>
<div class="abs top-line"></div>
<header class="abs site-header"></header>
<div class="abs brand"><span class="brand-dot"></span>VELMORIX</div>
<nav>
  <span class="abs nav pill nav-home">Home</span>
  <span class="abs nav" style="left:752px">About Us</span>
  <span class="abs nav" style="left:864px">Products</span>
  <span class="abs nav" style="left:982px">Contact Us</span>
</nav>

<div class="abs hero" role="img" aria-label="Olive oil being poured over a fresh salad"></div>
<div class="abs hero-base" role="img" aria-label="Salad with tomatoes, cheese and onion"></div>
<div class="abs hero-caption">Light and healthy with low<br>saturated fat ratio.</div>

<h1 class="abs section-title" style="top:804px">Welcome to Velmorix</h1>
<div class="abs intro">
  <p>VELMORIX is a manufacturing and trading company in Wrocław, Poland<br>
  We established longer and closer working relationships with our clients and supplier not only provide immediate and reliable service but to continually exceed expectations and goals.<br>
  We create commercial flows, import and export products, arranging and managing international projects with our partners.</p>
  <p style="margin-top:27px">Supported our network, we are able to integrate all these functions with our fruitful experience. Our numerous competencies allow us to respond to the needs of industries looking for a new market.</p>
</div>
<a class="abs pill btn" style="left:503px;top:1142px">Read More</a>

<h2 class="abs section-title" style="top:1234px">Categories</h2>
<div class="abs cat" style="left:107px;top:1369px;width:226px;height:224px"><div class="cat-fill" role="img" aria-label="Bottle of edible oil with olives" style="background:radial-gradient(circle,#e6cf5a 0%,#c7b45a 30%,#fff 70%)"></div></div>
<div class="abs cat" style="left:361px;top:1340px;width:225px;height:284px"><div class="cat-fill" role="img" aria-label="Ketchup bowl with tomatoes and spices" style="bottom:78px;background:radial-gradient(circle,#d42a2a 0%,#e85a50 35%,#fff 72%)"></div><div class="cat-label">Ketchup</div></div>
<div class="abs cat" style="left:614px;top:1369px;width:225px;height:224px"><div class="cat-fill" role="img" aria-label="Bowl of mayonnaise with lemon and eggs" style="background:radial-gradient(circle,#f5e7a0 0%,#f0d98a 35%,#fff 72%)"></div></div>
<div class="abs cat" style="left:867px;top:1369px;width:225px;height:224px"><div class="cat-fill" role="img" aria-label="Bowls of assorted pulses and lentils" style="background:radial-gradient(circle,#b07040 0%,#8a5a3a 35%,#fff 72%)"></div></div>

<div class="abs warehouse" role="img" aria-label="Warehouse interior with stacked pallets and a truck"></div>
<div class="abs band-title">We are a food stuff import &amp; export</div>
<a class="abs pill btn" style="left:503px;top:2027px">Get Started</a>

<h2 class="abs section-title" style="top:2356px">Products</h2>
<div class="abs product" style="left:107px;top:2455px;width:226px;height:283px"><div class="product-fill" role="img" aria-label="5 litre bottle of edible oil" style="background:radial-gradient(ellipse,#f3c63a 0%,#f5d97a 40%,#fff 75%)"></div></div>
<div class="abs product" style="left:364px;top:2455px;width:225px;height:283px"><div class="product-fill" role="img" aria-label="10 kg bucket of ketchup" style="background:radial-gradient(ellipse,#c23a3a 0%,#e8c0b0 45%,#fff 75%)"></div></div>
<div class="abs product" style="left:618px;top:2455px;width:225px;height:283px"><div class="product-fill" role="img" aria-label="10 kg bucket of mayonnaise" style="background:radial-gradient(ellipse,#e8dcc8 0%,#f0e8da 45%,#fff 75%)"></div></div>
<div class="abs product" style="left:873px;top:2455px;width:225px;height:283px"><div class="product-fill" role="img" aria-label="Heap of split dal lentils" style="background:radial-gradient(ellipse,#d9a040 0%,#ecc88a 40%,#fff 72%)"></div></div>
<div class="abs product-name" style="left:107px">PET 5000 ML</div>
<div class="abs product-name" style="left:364px">KETCHUP 10 KG</div>
<div class="abs product-name" style="left:618px">MAYONNAISE&nbsp; 10 KG</div>
<div class="abs product-name" style="left:873px">DAL</div>

<div class="abs map" role="img" aria-label="Street map showing the Wrocław office location"></div>

<h2 class="abs contact-title">Contact Us</h2>
<div class="abs col-head" style="left:128px">Office</div>
<div class="abs col-head" style="left:473px">Warehouse Poland</div>
<div class="abs col-head" style="left:773px">Warehouse&nbsp; Germany</div>

<svg width="0" height="0" style="position:absolute"><defs>
<symbol id="pin" viewBox="0 0 24 24"><path d="M12 2a7 7 0 0 0-7 7c0 5 7 13 7 13s7-8 7-13a7 7 0 0 0-7-7zm0 9.5a2.5 2.5 0 1 1 0-5 2.5 2.5 0 0 1 0 5z" fill="#2b2b2b"/></symbol>
<symbol id="phone" viewBox="0 0 24 24"><path d="M6.6 10.8a15 15 0 0 0 6.6 6.6l2.2-2.2c.3-.3.7-.4 1-.2 1.1.4 2.3.6 3.6.6.6 0 1 .4 1 1V20c0 .6-.4 1-1 1C10.6 21 3 13.4 3 4c0-.6.4-1 1-1h3.5c.6 0 1 .4 1 1 0 1.3.2 2.5.6 3.6.1.3 0 .7-.2 1z" fill="#2b2b2b"/></symbol>
</defs></svg>

<div class="abs line" style="left:125px;top:3545px"><svg width="13" height="15"><use href="#pin"/></svg><span>ul. Lipowa 12/4<br><span style="display:block;margin-top:9px">50-100 Wrocław Polska</span></span></div>
<div class="abs line" style="left:125px;top:3608px"><svg width="13" height="15"><use href="#phone"/></svg><span>Phone : +48 700 100 200</span></div>

<div class="abs line" style="left:473px;top:3545px;font-size:15px"><svg width="13" height="15"><use href="#pin"/></svg><span>ul. Polna 8, 55-300<br>Środa Śląska ,Poland</span></div>
<div class="abs line" style="left:473px;top:3611px"><svg width="13" height="15"><use href="#phone"/></svg></div>

<div class="abs line" style="left:773px;top:3545px;font-size:15px"><svg width="13" height="15"><use href="#pin"/></svg><span>Industriestraße 5, 50126<br>Bergheim, Germany</span></div>
<div class="abs line" style="left:773px;top:3611px;font-size:15px"><svg width="13" height="15"><use href="#phone"/></svg><span>Phone : +49 170 000 1234</span></div>

<footer class="abs site-footer">© 2020 &nbsp;|&nbsp; www.velmorix.pl</footer>
</body>
</html>
```